Real Estate Marketing Postcard Design

I'd like to advertise I'm a realtor and would like to provide some type of marketing information on the card that customers will keep as reference. Something Renters can use?
Updates

This needs to be a direct mail, no envelopes. Thanks!

Target Market(s)

Renters in Gainesville, Haymarket, Bristow, Centreville

Industry/Entity Type

Marketing

Requirements
Must have
• My name
Title
Brokerage Info
Number
Email

```html
<!DOCTYPE html>
<html lang="en">
<head>
<meta charset="utf-8">
<title>Hearthstone Realty – Calendar Postcard</title>
<link href="https://fonts.googleapis.com/css2?family=Arvo:wght@700&family=Roboto:wght@400;500;700&display=swap" rel="stylesheet">
<style>
  :root {
    --stage: #e9e9e9;
    --label: #c9c9c9;
    --charcoal: #242424;
    --charcoal-soft: #2e2e2e;
    --gold: #c9a23f;
    --gold-muted: #a38d55;
    --white: #ffffff;
    --ink: #2b2b2b;
    --grey-text: #d4d4d4;
    --photo-top: #a9c6e4;
    --photo-bottom: #6f9b4a;
    --portrait: #9a7766;
  }
  * { box-sizing: border-box; margin: 0; padding: 0; }
  html, body { width: 1200px; height: 595px; overflow: hidden; }
  body {
    position: relative;
    background: var(--stage);
    font-family: "Roboto", Arial, sans-serif;
  }
  .side-label {
    position: absolute; top: 92px;
    font: 700 16px/1 "Roboto", sans-serif;
    color: var(--label); letter-spacing: .5px;
  }

  /* ---------- Front ---------- */
  .front {
    position: absolute; left: 96px; top: 122px; width: 462px; height: 360px;
    background: var(--charcoal); overflow: hidden;
  }
  .front .top-band { position: absolute; inset: 0 0 auto 0; height: 116px; background: var(--charcoal-soft); }
  .front .gold-rule { position: absolute; left: 0; right: 0; top: 116px; height: 5px; background: var(--gold); }
  .brand-ribbon {
    position: absolute; left: 32px; top: 0; width: 90px; height: 88px;
    background: var(--white);
    clip-path: polygon(0 0,100% 0,100% 100%,50% 80%,0 100%);
    display: flex; align-items: center; justify-content: center;
    padding-bottom: 18px;
  }
  .brand-ribbon .brand-name { font: 700 10px/1.15 "Arvo", serif; color: var(--gold); text-align: center; }
  .headline {
    position: absolute; right: 28px; top: 18px; text-align: right;
    font: 700 24px/28px "Arvo", serif; color: var(--gold); letter-spacing: .3px;
  }
  .call-line {
    position: absolute; right: 28px; top: 80px;
    font: 400 18px/1 "Roboto", sans-serif; color: var(--gold-muted);
  }
  .agent-panel { position: absolute; left: 0; top: 121px; width: 153px; bottom: 0; background: var(--charcoal); color: var(--white); }
  .agent-portrait {
    position: absolute; left: 39px; top: 11px; width: 72px; height: 72px; border-radius: 50%;
    background: var(--portrait); border: 2px solid var(--white);
  }
  .agent-name { position: absolute; left: 0; width: 100%; top: 98px; text-align: center; font: 500 13px/1 "Roboto", sans-serif; letter-spacing: .4px; }
  .agent-dash { position: absolute; left: 70px; top: 118px; width: 13px; height: 2px; background: var(--white); }
  .agent-title { position: absolute; left: 0; width: 100%; top: 127px; text-align: center; font: 400 9px/12px "Roboto", sans-serif; color: var(--grey-text); }
  .contact-list { position: absolute; left: 30px; top: 166px; list-style: none; font: 400 6.5px/8px "Roboto", sans-serif; color: var(--grey-text); }
  .contact-list li { display: flex; align-items: flex-start; gap: 6px; margin-bottom: 6px; }
  .contact-list svg { width: 7px; height: 7px; flex: none; fill: var(--white); }
  .home-photo {
    position: absolute; left: 153px; top: 121px; right: 0; bottom: 0;
    background: linear-gradient(180deg, var(--photo-top) 0%, var(--photo-bottom) 100%);
  }
  .visit-line {
    position: absolute; right: 26px; bottom: 26px;
    font: 400 13px/1 "Roboto", sans-serif; color: #111;
  }
  .visit-line strong { font-weight: 700; text-decoration: underline; }

  /* ---------- Back ---------- */
  .back {
    position: absolute; left: 647px; top: 122px; width: 461px; height: 360px;
    background: var(--white);
  }
  .back .gold-edge { position: absolute; right: 0; top: 0; bottom: 0; width: 12px; background: var(--gold); }
  .back-brand { position: absolute; right: 186px; top: 19px; text-align: right; }
  .back-brand .brand-name { font: 700 16px/1 "Arvo", serif; color: var(--gold); }
  .back-brand .brand-web { font: 400 14px/1 "Roboto", sans-serif; color: var(--gold); margin-top: 6px; }
  .year-slash { position: absolute; left: 287px; top: 18px; font: 700 36px/1 "Arvo", serif; color: var(--gold); }
  .year { position: absolute; left: 322px; top: 18px; font: 700 40px/1 "Arvo", serif; color: var(--ink); }
  .month { position: absolute; width: 93px; color: var(--ink); }
  .month h3 { text-align: right; font: 700 9px/1 "Roboto", sans-serif; letter-spacing: .2px; }
  .month h3::after { content: ""; display: block; margin: 3px 0 0 auto; width: 8px; height: 2px; background: var(--ink); }
  .week, .days { display: grid; grid-template-columns: repeat(7, 1fr); text-align: center; font: 400 7.5px/10px "Roboto", sans-serif; }
  .week { font-weight: 700; margin-top: 5px; }
  .days span:first-child { grid-column: 5; }
</style>
</head>
<body>
  <div class="side-label" style="left:97px">FRONT</div>
  <div class="side-label" style="left:648px">BACK</div>

  <section class="front">
    <div class="top-band"></div>
    <div class="gold-rule"></div>
    <div class="brand-ribbon"><span class="brand-name">HEARTHSTONE<br>REALTY</span></div>
    <h1 class="headline">LOOKING FOR YOUR<br>DREAM HOUSE?</h1>
    <p class="call-line">CALL 555-014-2290</p>

    <div class="agent-panel">
      <div class="agent-portrait" role="img" aria-label="Portrait photo of the agent"></div>
      <p class="agent-name">DANA WHITFIELD</p>
      <div class="agent-dash"></div>
      <p class="agent-title">REALTOR<br>LICENSED IN VIRGINIA</p>
      <ul class="contact-list">
        <li><svg viewBox="0 0 10 10"><path d="M5 0a3.5 3.5 0 0 0-3.5 3.5C1.5 6 5 10 5 10s3.5-4 3.5-6.5A3.5 3.5 0 0 0 5 0zm0 5a1.5 1.5 0 1 1 0-3 1.5 1.5 0 0 1 0 3z"/></svg><span>1180 LARKSPUR LANE<br>NORTHFIELD, VA 20100</span></li>
        <li><svg viewBox="0 0 10 10"><path d="M3 0h4a1 1 0 0 1 1 1v8a1 1 0 0 1-1 1H3a1 1 0 0 1-1-1V1a1 1 0 0 1 1-1zm0 1.5v6h4v-6z"/></svg><span>555-014-2290</span></li>
        <li><svg viewBox="0 0 10 10"><path d="M1 3h8v6H1zM2.5 0h5v2.5h-5zM3 5h4v1H3zm0 2h4v1H3z"/></svg><span>555-018-3341</span></li>
        <li><svg viewBox="0 0 10 10"><path d="M0 2h10v6H0zm1 1v.3l4 2.4 4-2.4V3z"/></svg><span>DWHITFIELD@MAILBOX.COM</span></li>
      </ul>
    </div>

    <div class="home-photo" role="img" aria-label="Photo of a stone-front family house with a green lawn under a blue sky"></div>
    <p class="visit-line">VISIT <strong>HEARTHSTONEREALTY.COM</strong></p>
  </section>

  <section class="back">
    <div class="gold-edge"></div>
    <div class="back-brand">
      <p class="brand-name">HEARTHSTONE REALTY</p>
      <p class="brand-web">HEARTHSTONEREALTY.COM</p>
    </div>
    <div class="year-slash">//</div>
    <div class="year">2015</div>

    <div class="month" style="left:27px;top:78px"><h3>JANUARY</h3><div class="week"><span>S</span><span>M</span><span>T</span><span>W</span><span>T</span><span>F</span><span>S</span></div><div class="days"><span>1</span><span>2</span><span>3</span><span>4</span><span>5</span><span>6</span><span>7</span><span>8</span><span>9</span><span>10</span><span>11</span><span>12</span><span>13</span><span>14</span><span>15</span><span>16</span><span>17</span><span>18</span><span>19</span><span>20</span><span>21</span><span>22</span><span>23</span><span>24</span><span>25</span><span>26</span><span>27</span><span>28</span><span>29</span><span>30</span><span>31</span></div></div>
    <div class="month" style="left:126px;top:78px"><h3>FEBRUARY</h3><div class="week"><span>S</span><span>M</span><span>T</span><span>W</span><span>T</span><span>F</span><span>S</span></div><div class="days"><span>1</span><span>2</span><span>3</span><span>4</span><span>5</span><span>6</span><span>7</span><span>8</span><span>9</span><span>10</span><span>11</span><span>12</span><span>13</span><span>14</span><span>15</span><span>16</span><span>17</span><span>18</span><span>19</span><span>20</span><span>21</span><span>22</span><span>23</span><span>24</span><span>25</span><span>26</span><span>27</span><span>28</span><span>29</span><span>30</span><span>31</span></div></div>
    <div class="month" style="left:227px;top:78px"><h3>MARCH</h3><div class="week"><span>S</span><span>M</span><span>T</span><span>W</span><span>T</span><span>F</span><span>S</span></div><div class="days"><span>1</span><span>2</span><span>3</span><span>4</span><span>5</span><span>6</span><span>7</span><span>8</span><span>9</span><span>10</span><span>11</span><span>12</span><span>13</span><span>14</span><span>15</span><span>16</span><span>17</span><span>18</span><span>19</span><span>20</span><span>21</span><span>22</span><span>23</span><span>24</span><span>25</span><span>26</span><span>27</span><span>28</span><span>29</span><span>30</span><span>31</span></div></div>
    <div class="month" style="left:328px;top:78px"><h3>APRIL</h3><div class="week"><span>S</span><span>M</span><span>T</span><span>W</span><span>T</span><span>F</span><span>S</span></div><div class="days"><span>1</span><span>2</span><span>3</span><span>4</span><span>5</span><span>6</span><span>7</span><span>8</span><span>9</span><span>10</span><span>11</span><span>12</span><span>13</span><span>14</span><span>15</span><span>16</span><span>17</span><span>18</span><span>19</span><span>20</span><span>21</span><span>22</span><span>23</span><span>24</span><span>25</span><span>26</span><span>27</span><span>28</span><span>29</span><span>30</span><span>31</span></div></div>

    <div class="month" style="left:27px;top:171px"><h3>MAY</h3><div class="week"><span>S</span><span>M</span><span>T</span><span>W</span><span>T</span><span>F</span><span>S</span></div><div class="days"><span>1</span><span>2</span><span>3</span><span>4</span><span>5</span><span>6</span><span>7</span><span>8</span><span>9</span><span>10</span><span>11</span><span>12</span><span>13</span><span>14</span><span>15</span><span>16</span><span>17</span><span>18</span><span>19</span><span>20</span><span>21</span><span>22</span><span>23</span><span>24</span><span>25</span><span>26</span><span>27</span><span>28</span><span>29</span><span>30</span><span>31</span></div></div>
    <div class="month" style="left:126px;top:171px"><h3>JUNE</h3><div class="week"><span>S</span><span>M</span><span>T</span><span>W</span><span>T</span><span>F</span><span>S</span></div><div class="days"><span>1</span><span>2</span><span>3</span><span>4</span><span>5</span><span>6</span><span>7</span><span>8</span><span>9</span><span>10</span><span>11</span><span>12</span><span>13</span><span>14</span><span>15</span><span>16</span><span>17</span><span>18</span><span>19</span><span>20</span><span>21</span><span>22</span><span>23</span><span>24</span><span>25</span><span>26</span><span>27</span><span>28</span><span>29</span><span>30</span><span>31</span></div></div>
    <div class="month" style="left:227px;top:171px"><h3>JULY</h3><div class="week"><span>S</span><span>M</span><span>T</span><span>W</span><span>T</span><span>F</span><span>S</span></div><div class="days"><span>1</span><span>2</span><span>3</span><span>4</span><span>5</span><span>6</span><span>7</span><span>8</span><span>9</span><span>10</span><span>11</span><span>12</span><span>13</span><span>14</span><span>15</span><span>16</span><span>17</span><span>18</span><span>19</span><span>20</span><span>21</span><span>22</span><span>23</span><span>24</span><span>25</span><span>26</span><span>27</span><span>28</span><span>29</span><span>30</span><span>31</span></div></div>
    <div class="month" style="left:328px;top:171px"><h3>AUGUST</h3><div class="week"><span>S</span><span>M</span><span>T</span><span>W</span><span>T</span><span>F</span><span>S</span></div><div class="days"><span>1</span><span>2</span><span>3</span><span>4</span><span>5</span><span>6</span><span>7</span><span>8</span><span>9</span><span>10</span><span>11</span><span>12</span><span>13</span><span>14</span><span>15</span><span>16</span><span>17</span><span>18</span><span>19</span><span>20</span><span>21</span><span>22</span><span>23</span><span>24</span><span>25</span><span>26</span><span>27</span><span>28</span><span>29</span><span>30</span><span>31</span></div></div>

    <div class="month" style="left:27px;top:264px"><h3>SEMPTEMBER</h3><div class="week"><span>S</span><span>M</span><span>T</span><span>W</span><span>T</span><span>F</span><span>S</span></div><div class="days"><span>1</span><span>2</span><span>3</span><span>4</span><span>5</span><span>6</span><span>7</span><span>8</span><span>9</span><span>10</span><span>11</span><span>12</span><span>13</span><span>14</span><span>15</span><span>16</span><span>17</span><span>18</span><span>19</span><span>20</span><span>21</span><span>22</span><span>23</span><span>24</span><span>25</span><span>26</span><span>27</span><span>28</span><span>29</span><span>30</span><span>31</span></div></div>
    <div class="month" style="left:126px;top:264px"><h3>OCTOBER</h3><div class="week"><span>S</span><span>M</span><span>T</span><span>W</span><span>T</span><span>F</span><span>S</span></div><div class="days"><span>1</span><span>2</span><span>3</span><span>4</span><span>5</span><span>6</span><span>7</span><span>8</span><span>9</span><span>10</span><span>11</span><span>12</span><span>13</span><span>14</span><span>15</span><span>16</span><span>17</span><span>18</span><span>19</span><span>20</span><span>21</span><span>22</span><span>23</span><span>24</span><span>25</span><span>26</span><span>27</span><span>28</span><span>29</span><span>30</span><span>31</span></div></div>
    <div class="month" style="left:227px;top:264px"><h3>NOVEMBER</h3><div class="week"><span>S</span><span>M</span><span>T</span><span>W</span><span>T</span><span>F</span><span>S</span></div><div class="days"><span>1</span><span>2</span><span>3</span><span>4</span><span>5</span><span>6</span><span>7</span><span>8</span><span>9</span><span>10</span><span>11</span><span>12</span><span>13</span><span>14</span><span>15</span><span>16</span><span>17</span><span>18</span><span>19</span><span>20</span><span>21</span><span>22</span><span>23</span><span>24</span><span>25</span><span>26</span><span>27</span><span>28</span><span>29</span><span>30</span><span>31</span></div></div>
    <div class="month" style="left:328px;top:264px"><h3>DECEMBER</h3><div class="week"><span>S</span><span>M</span><span>T</span><span>W</span><span>T</span><span>F</span><span>S</span></div><div class="days"><span>1</span><span>2</span><span>3</span><span>4</span><span>5</span><span>6</span><span>7</span><span>8</span><span>9</span><span>10</span><span>11</span><span>12</span><span>13</span><span>14</span><span>15</span><span>16</span><span>17</span><span>18</span><span>19</span><span>20</span><span>21</span><span>22</span><span>23</span><span>24</span><span>25</span><span>26</span><span>27</span><span>28</span><span>29</span><span>30</span><span>31</span></div></div>
  </section>
</body>
</html>
```